Business Card Design Project

I run holistic health workshops, speaking engagements, group and 1on1 coaching, cooking classes, and am a speaker and presenter on holistic health topics.

I would like professionally designed business cards using the attached logo. I would like the reverse of the cards to use the leaf pattern blown up large across the back of the card as the design. I'd also like to use the words "mind.body.spirit.nutrition" across the backside of the cards.

The front of the cards should contain the following contact details:
Megan Thorsby-Kell
Founder & President
The Harwick Advisory Group
+61 477 392 604
theharwickadvisorygroup@mailbrook.example

Target Market(s)

Corporate HR, Health & wellness businesses, upmarket spas, other businesses in the holistic health & wellness fields looking for a speaker/presenter/workshop leader

Industry/Entity Type

Cooking

Requirements
Must have
• Must use the attached design; must use earth tones in line with the logo (browns/greens/blues/tans)

```html
<!DOCTYPE html>
<html lang="en">
<head>
<meta charset="utf-8">
<title>Harwick Advisory Group – Business Card Options</title>
<link rel="stylesheet" href="https://fonts.googleapis.com/css2?family=Roboto+Condensed:wght@400;700&display=swap">
<style>
  :root {
    --sheet: #ffffff;
    --sheet-edge: #9a9a9a;
    --card-edge: #1e1e1e;
    --lime: #8cc63f;
    --lime-deep: #5aab2e;
    --forest: #0f9342;
    --forest-light: #7dc242;
    --ink: #1c1c1c;
    --logo-ink: #4b4842;
    --white: #ffffff;
    --band-dark: #1f3a12;
    --ornament-light: rgba(255,255,255,0.22);
    --ornament-clear: rgba(255,255,255,0);
  }
  * { box-sizing: border-box; margin: 0; padding: 0; }
  html, body { width: 1200px; height: 636px; overflow: hidden; background: var(--sheet); }
  .sheet {
    position: relative; width: 1200px; height: 636px;
    border: 1px solid var(--sheet-edge);
    font-family: "Roboto Condensed", "Arial Narrow", sans-serif;
  }
  .card { position: absolute; border-radius: 14px; overflow: hidden; }

  /* Front A */
  .front-a { left: 95px; top: 40px; width: 486px; height: 273px; background: var(--white); border: 1px solid var(--card-edge); }
  .front-a .panel {
    position: absolute; left: 12px; top: 9px; width: 457px; height: 253px; border-radius: 10px;
    background: linear-gradient(100deg, var(--lime) 0%, var(--lime-deep) 100%); overflow: hidden;
  }
  .front-a .holder { position: absolute; left: 26px; top: 31px; color: var(--white); font-weight: 700; font-size: 15px; line-height: 19px; }
  .front-a .company { position: absolute; left: 22px; top: 111px; color: var(--ink); font-weight: 700; font-size: 25px; }
  .front-a .contact-band {
    position: absolute; left: 14px; top: 199px; width: 370px; height: 44px;
    background: linear-gradient(90deg, var(--band-dark) 0%, rgba(31,58,18,0.75) 55%, rgba(31,58,18,0) 100%);
    border-left: 3px solid var(--white);
  }
  .front-a .contact { position: absolute; left: 22px; top: 201px; color: var(--white); font-weight: 700; font-size: 14px; line-height: 19px; }
  .front-a .ornament {
    position: absolute; right: -10px; top: 0; width: 130px; height: 253px;
    background: radial-gradient(ellipse 60% 55% at 60% 50%, var(--ornament-light), var(--ornament-clear) 100%);
  }

  /* Front B */
  .front-b {
    left: 622px; top: 40px; width: 485px; height: 273px; border: 1px solid var(--card-edge);
    background: linear-gradient(30deg, var(--forest-light) 0%, var(--forest) 100%);
  }
  .tab { position: absolute; width: 11px; height: 205px; background: var(--white); top: 33px; border-radius: 6px; }
  .tab.left { left: -2px; } .tab.right { right: -2px; }
  .front-b .holder { position: absolute; left: 38px; top: 41px; color: var(--white); font-weight: 700; font-size: 15px; line-height: 19px; }
  .front-b .company { position: absolute; left: 90px; top: 120px; color: var(--white); font-weight: 700; font-size: 23px; }
  .front-b .contact { position: absolute; right: 27px; top: 206px; color: var(--white); font-weight: 700; font-size: 14px; line-height: 17px; text-align: right; }
  .front-b .ornament {
    position: absolute; left: 0; top: 140px; width: 160px; height: 133px;
    background: radial-gradient(ellipse 50% 50% at 45% 60%, var(--ornament-light), var(--ornament-clear) 100%);
  }

  /* Backs */
  .back-a { left: 95px; top: 322px; width: 486px; height: 276px; background: var(--lime); border: 1px solid var(--card-edge); }
  .back-a .panel { position: absolute; left: 12px; top: 9px; width: 457px; height: 253px; background: var(--white); border-radius: 14px; }
  .back-b { left: 622px; top: 322px; width: 485px; height: 276px; background: var(--white); border: 1px solid var(--card-edge); }
  .bar { position: absolute; top: 32px; width: 14px; height: 207px; background: var(--lime); }
  .bar.left { left: 0; } .bar.right { right: 0; }

  .brand { position: absolute; right: 24px; top: 96px; display: flex; align-items: center; gap: 12px; }
  .back-b .brand { right: 30px; top: 105px; }
  .brand-dot { width: 22px; height: 22px; border-radius: 50%; background: var(--lime); }
  .brand-name { color: var(--logo-ink); font-weight: 700; font-size: 50px; letter-spacing: 0.5px; }
</style>
</head>
<body>
<main class="sheet">
  <section class="card front-a">
    <div class="panel">
      <div class="ornament" role="img" aria-label="Pale swirling vine and leaf ornament"></div>
      <p class="holder">Megan Thorsby-Kell<br>Founder &amp; President</p>
      <h2 class="company">The Harwick Advisory Group</h2>
      <div class="contact-band"></div>
      <p class="contact">[m] +61 477 392 604<br>[e] theharwickadvisorygroup@mailbrook.example</p>
    </div>
  </section>

  <section class="card front-b">
    <div class="ornament" role="img" aria-label="White swirling vine and leaf ornament"></div>
    <span class="tab left"></span><span class="tab right"></span>
    <p class="holder">Megan Thorsby-Kell<br>Founder &amp; President</p>
    <h2 class="company">The Harwick Advisory Group</h2>
    <p class="contact">[m] +61 477 392 604<br>[e] theharwickadvisorygroup@mailbrook.example</p>
  </section>

  <section class="card back-a">
    <div class="panel">
      <div class="brand"><span class="brand-dot"></span><span class="brand-name">Harwick Group</span></div>
    </div>
  </section>

  <section class="card back-b">
    <span class="bar left"></span><span class="bar right"></span>
    <div class="brand"><span class="brand-dot"></span><span class="brand-name">Harwick Group</span></div>
  </section>
</main>
</body>
</html>
```